CBD Product Label Supplement Company

We need a label design for our CBD Immunity Gummies product. The CBD immunity gummies are strawberry flavored. Here's an example of one the top brands currently. https://www.brindlefarrow.example/cbd-melatonin-sleep-gummy. Please don't make it look similar to that brand. That is just an example of a top brand currently. Our brand colors is simply green and white, logo included in files. We don't want a lot of colors in the design and don't want the design to be all over the place. we want multi colors 4 maybe 5 used. target audience is 30 years and older. Want to give it a nature feel while also conveying immunity. Attached screenshot will show standard label with ingredients and designations. We'd like all of those included on the label if possible. Vegetarian, Vegan, Non-Dairy, Gluten free, Non-Gmo. Ad " Vitamin C + Elderberry" to front of label as well.

Target Market(s)

30 to 65+ men and women. Pain Relief and Immunity Support Focused.

Industry/Entity Type

Supplement

Font styles to use
Serif
Sans Serif

Colors
9bcb3c
add136
00a990
33b8a4
ec1f27
f04a50
ffffff
6b449b

Requirements
Must have
• Informative label. Because we've combined CBD with Elderberry, Vitamin C, Vitamin A, Vitamin E to help with Immunity we want that to be known. Elderberry, Vitamin C are the two most important vitamins of that mix. Product designation labels, Vegetarian, Vegan, Non-Dairy, Gluten free, Non-Gmo. Gummies are strawberry flavored so would like some redish, pink somewhere in label.
Should not have
• no browns, grays, oranges, yellow,

```html
<!DOCTYPE html>
<html lang="en">
<head>
<meta charset="UTF-8">
<title>Leafora Nutrition – CBD Immunity Gummies Label</title>
<link href="https://fonts.googleapis.com/css2?family=Roboto+Condensed:wght@400;700&family=Roboto:wght@300;400;700&display=swap" rel="stylesheet">
<style>
  :root{
    --purple:#6b449b;
    --purple-deep:#4f2f7e;
    --green:#9bcb3c;
    --green-mid:#add136;
    --green-deep:#4d9e3a;
    --red:#ec1f27;
    --red-soft:#f04a50;
    --white:#ffffff;
    --ink:#1d1d1d;
  }
  html,body{margin:0;padding:0;width:1200px;height:1200px;overflow:hidden;background:var(--white);}
  .canvas{position:relative;width:1200px;height:1200px;background:var(--white);font-family:"Roboto Condensed",sans-serif;}
  .label{position:absolute;left:60px;top:300px;width:1080px;height:600px;overflow:hidden;box-shadow:0 0 0 1px rgba(0,0,0,.06);}
  .label__main{position:absolute;left:0;top:0;width:100%;height:450px;
    background:radial-gradient(ellipse at 50% 45%, #8660b4 0%, var(--purple) 45%, var(--purple-deep) 100%);}
  .label__band{position:absolute;left:0;top:450px;width:100%;height:150px;
    background:linear-gradient(180deg, #8cc45e 0%, var(--green-deep) 100%);}

  .front{position:absolute;left:300px;top:0;width:480px;height:600px;text-align:center;color:var(--white);}
  .brand{position:absolute;top:46px;left:0;width:100%;display:flex;justify-content:center;align-items:center;gap:12px;}
  .brand__name{font-family:"Roboto",sans-serif;font-weight:300;font-size:40px;color:var(--white);letter-spacing:.5px;line-height:1;}
  .brand__dot{width:30px;height:30px;border-radius:50%;background:var(--green);}
  .title{position:absolute;top:128px;left:0;width:100%;margin:0;font-weight:700;font-size:66px;line-height:68px;letter-spacing:-.5px;}
  .flavor{position:absolute;top:284px;left:50%;transform:translateX(-50%);padding:6px 22px;border-radius:24px;
    background:linear-gradient(180deg,var(--red-soft),#d8303a);font-weight:700;font-size:30px;line-height:36px;white-space:nowrap;}
  .tagline{position:absolute;top:346px;left:0;width:100%;font-weight:700;font-size:26px;}
  .specs{position:absolute;top:390px;left:0;width:100%;font-weight:400;font-size:19px;line-height:23px;}
  .count{position:absolute;top:474px;left:0;width:100%;font-weight:700;font-size:36px;line-height:44px;}

  .badges{position:absolute;left:232px;top:150px;display:flex;flex-direction:column;gap:14px;}
  .badge{width:58px;height:58px;border-radius:50%;border:3px solid var(--green);box-sizing:border-box;
    display:flex;align-items:center;justify-content:center;text-align:center;color:var(--white);
    font-weight:700;font-size:11px;line-height:12px;}

  .directions{position:absolute;left:236px;top:470px;width:56px;height:90px;background:var(--white);
    color:var(--ink);font-size:10px;line-height:12px;padding:6px 4px;box-sizing:border-box;}

  .facts{position:absolute;left:812px;top:22px;width:240px;height:556px;background:var(--white);color:var(--ink);
    box-sizing:border-box;padding:12px 14px;font-family:"Roboto",sans-serif;font-size:13px;line-height:17px;}
  .facts__title{font-family:"Roboto Condensed",sans-serif;font-weight:700;font-size:26px;line-height:30px;margin:0 0 4px;}
  .facts__rule{border-top:1px solid var(--ink);margin:4px 0;}
  .facts__rule--thick{border-top:6px solid var(--ink);}
  .facts__row{display:flex;justify-content:space-between;border-bottom:1px solid #999;padding:4px 0;}
  .facts__head{font-weight:700;}
  .facts__other{margin-top:10px;font-size:12px;line-height:16px;}
</style>
</head>
<body>
<div class="canvas">
  <section class="label" aria-label="CBD Immunity Gummies label">
    <div class="label__main"></div>
    <div class="label__band"></div>

    <div class="badges">
      <div class="badge">VEGAN</div>
      <div class="badge">NON-<br>DAIRY</div>
      <div class="badge">GLUTEN<br>FREE</div>
      <div class="badge">NON-<br>GMO</div>
    </div>

    <div class="directions">Take 1 gummy daily.</div>

    <div class="front">
      <div class="brand">
        <span class="brand__name">Leafora Nutrition</span>
        <span class="brand__dot"></span>
      </div>
      <h1 class="title">CBD Immunity<br>Gummies</h1>
      <div class="flavor">Strawberry Flavor</div>
      <div class="tagline">Pain Relief and Immunity Support</div>
      <div class="specs">10mg CBD per serving<br>Vitamin C + Elderberry</div>
      <div class="count">30 Gummies<br>Dietary Supplement</div>
    </div>

    <aside class="facts">
      <h2 class="facts__title">Supplement Facts</h2>
      <div>Serving Size: 1 Gummy</div>
      <div>Servings Per Container: 30</div>
      <div class="facts__rule facts__rule--thick"></div>
      <div class="facts__row facts__head"><span>Amount Per Serving</span><span>% DV</span></div>
      <div class="facts__row"><span>Vitamin A 300 mcg</span><span>33%</span></div>
      <div class="facts__row"><span>Vitamin C 60 mg</span><span>67%</span></div>
      <div class="facts__row"><span>Vitamin E 10 mg</span><span>67%</span></div>
      <div class="facts__row"><span>Elderberry Extract 50 mg</span><span>*</span></div>
      <div class="facts__row"><span>Hemp Extract (CBD) 10 mg</span><span>*</span></div>
      <div class="facts__rule facts__rule--thick"></div>
      <div class="facts__other">Other Ingredients: Pectin, Cane Sugar, Natural Flavor.</div>
    </aside>
  </section>
</div>
</body>
</html>
```